Corporate Identity Pack - LetterHead, Business Card, Envelope

We are looking for a clean, professional, and visually connected corporate identity set for our company "VELTA HOME" (Cleaning, Gardening, and Pest Control services).

The pack must include:

Business Card (front and back)
Envelope with recipient window on the right side (22x11)
A4 Letterhead

We provide:
Our final logo (PNG)
Three design references (Inspiration1, Inspiration2, Inspiration3) to spark ideas — but you are absolutely free to propose your own creative solutions based on these concepts.

What we want:
A clean, modern, and trustworthy style
A subtle but creative watermark or graphic detail on the letterhead (not too invasive)

The same visual "family feeling" across business card, envelope, and letterhead: designs must be different but clearly connected

Strong readability for all text and contact details

Use our brand colors (Navy Blue, Green, Orange/Red) in a smart, non-overloaded way

No strict limitations: we are open to creative proposals as long as they are coherent, elegant, and suitable for professional use

Technical specifications:
100% full A4 page layout (no accidental borders)

Deliver ready-to-print PDFs and vector files (AI, EPS)

Respect 5 mm safety margins

Standard sizes for A4, business card, envelope C6 with window at the right

Tone:
Modern – Clean – Elegant – Creative – Trustworthy

Target Market(s)

Professional businesses, property managers, condominium administrators, companies, clinics, and offices requiring cleaning, gardening, and pest control services. The design must convey trust, reliability, professionalism, and attention to detail.

Industry/Entity Type

Cleaning Services, Gardening Services, Pest Control Services

Colors
0054AA
0677BA
7BADD7
CADEEF
E8F1F8
59FF00
82FF00
B8FF75
E3FFCB
F4FFEA
EB3D1F
EC4F4E
F09395
F8D3D4
FCEDEE

Requirements
Must have
• Cohesive design across business card, letterhead, and envelope Clean, modern, professional look Use of brand colors: Navy Blue (main), Green, Orange/Red accents Letterhead must include a subtle watermark without interfering with text Envelope must be with a transparent window for recipient address visibility High readability of all text and contact details Proper alignment, no unnecessary margins (full A4 layout)
Nice to have
• Creative but discreet use of the checkmark from the logo as part of the background or watermark Slight variation or accent of color tones while respecting brand identity A clean visual accent that gives a sense of movement or dynamic professionalism (without being distracting) Icons for email, phone, and website on the business card (if stylistically appropriate)
Should not have
• Overuse of colors or rainbow effects Heavy backgrounds or complex textures that interfere with readability Fonts that are too playful, comic-style, or non-professional Overcrowded layouts — the design must feel clean and spacious Watermarks that are too strong or central (they must be subtle and marginal)

```html
<!DOCTYPE html>
<html lang="en">
<head>
<meta charset="utf-8">
<title>VELTA HOME – Corporate Identity</title>
<link href="https://fonts.googleapis.com/css2?family=Roboto:wght@400;700&display=swap" rel="stylesheet">
<style>
:root{
  --navy:#14127a;
  --green:#6cc93f;
  --orange:#f2631c;
  --paper:#f6f4f5;
  --ink:#2b2b33;
  --grey:#6b6b72;
  --stage:#3b3b3d;
  --wm-blue:#d9d8e6;
  --wm-green:#e3efd9;
}
*{margin:0;padding:0;box-sizing:border-box}
html,body{width:1200px;height:597px;overflow:hidden}
body{background:var(--stage);font-family:"Roboto",Arial,sans-serif;position:relative;color:var(--ink)}
.piece{position:absolute;overflow:hidden}
.wordmark{font-weight:700;color:var(--navy);white-space:nowrap;display:flex;align-items:center;gap:4px;letter-spacing:.02em}
.wordmark i{display:inline-block;background:var(--green)}
.icon{width:6px;height:6px;flex:none}
.contact{display:flex;align-items:center;gap:3px;white-space:nowrap}

/* business card front */
.card-front{left:44px;top:120px;width:256px;height:146px;background:#fff;border-radius:8px}
.card-front .wordmark{position:absolute;left:14px;top:64px;font-size:11px}
.card-front .wordmark i{width:9px;height:9px}
.card-front .panel{position:absolute;left:123px;top:0;right:0;bottom:0;background:var(--navy);border-left:3px solid var(--green);color:#fff;padding:24px 0 0 14px}
.card-front .name{color:var(--orange);font-weight:700;font-size:10px;letter-spacing:.02em}
.card-front .role{color:var(--green);font-size:5.5px;margin-top:1px}
.card-front .address{font-size:5.8px;line-height:7.6px;margin-top:9px}
.card-front .contacts{font-size:5.8px;line-height:7.6px;margin-top:6px}

/* business card back */
.card-back{left:39px;top:322px;width:261px;height:149px;background:#fff;border-radius:8px;display:flex;align-items:center;justify-content:center}
.card-back .wordmark{font-size:19px;gap:7px}
.card-back .wordmark i{width:16px;height:16px}

/* letterhead */
.letterhead{left:327px;top:52px;width:358px;height:504px;background:var(--paper)}
.letterhead .wordmark{position:absolute;left:22px;top:43px;font-size:11px}
.letterhead .wordmark i{width:9px;height:9px}
.letterhead .address{position:absolute;right:106px;top:34px;text-align:right;font-size:5.4px;line-height:7.3px;color:var(--ink)}
.letterhead .divider{position:absolute;left:258px;top:33px;width:.5px;height:30px;background:#888}
.letterhead .contacts{position:absolute;left:262px;top:34px;font-size:5.4px;line-height:7.3px}
.letterhead .watermark{position:absolute;left:52px;top:127px;width:254px;height:250px;background:linear-gradient(135deg,var(--wm-blue),var(--wm-green));opacity:.55}
.letterhead .body{position:absolute;left:35px;top:122px;width:290px}
.letterhead .greeting{font-size:9.5px;color:#555}
.letterhead .body p{font-size:5.2px;line-height:8.6px;color:#666;text-align:justify;margin-top:8.5px}
.letterhead .body p:first-of-type{margin-top:17px}
.letterhead .closing{position:absolute;left:35px;top:343px;font-size:5.5px;color:#666}
.letterhead .signature{position:absolute;left:33px;top:354px;width:48px;height:18px;background:#e4e2e4}
.letterhead .signer{position:absolute;left:37px;top:383px;font-size:8px;color:#555}
.letterhead .signer small{display:block;font-size:6px;margin-top:2px}
.letterhead .footer{position:absolute;left:0;right:0;bottom:0;height:15px;border-top:2px solid var(--green)}
.letterhead .footer div{position:absolute;left:0;right:0;bottom:0;height:11px;background:var(--navy);color:#fff;font-size:5.3px;text-align:center;line-height:11px}

/* envelope back */
.envelope-back{left:746px;top:169px;width:401px;height:183px;background:var(--paper)}
.envelope-back .flap{position:absolute;left:0;top:0;width:401px;height:67px}
.envelope-back .wordmark{position:absolute;left:0;right:0;top:24px;justify-content:center;color:#fff;font-size:11px}

/* envelope front */
.envelope-front{left:716px;top:266px;width:403px;height:183px;background:var(--paper);box-shadow:0 -2px 6px rgba(0,0,0,.15)}
.envelope-front .watermark{position:absolute;left:220px;top:8px;width:174px;height:161px;background:linear-gradient(135deg,var(--wm-blue),var(--wm-green));opacity:.55}
.envelope-front .window{position:absolute;left:211px;top:67px;width:158px;height:64px;border-radius:4px;background:rgba(255,255,255,.35);box-shadow:0 0 3px rgba(0,0,0,.18)}
.envelope-front .wordmark{position:absolute;left:25px;top:27px;font-size:13px}
.envelope-front .wordmark i{width:10px;height:10px}
.envelope-front .address{position:absolute;left:23px;top:90px;font-size:5.5px;line-height:7.3px}
.envelope-front .contacts{position:absolute;left:23px;top:127px;font-size:5.5px;line-height:7.3px}
.envelope-front .footer{position:absolute;left:0;right:0;bottom:0;height:14px;border-top:2px solid var(--green)}
.envelope-front .footer div{position:absolute;left:0;right:0;bottom:0;height:10px;background:var(--navy);color:#fff;font-size:5.3px;line-height:10px;padding-left:22px}
</style>
</head>
<body>
<svg width="0" height="0" style="position:absolute">
  <defs>
    <symbol id="i-phone" viewBox="0 0 10 10"><path d="M2 1l2 0 1 2.5-1.3 1a6 6 0 0 0 2.8 2.8l1-1.3L10 7v2c0 .5-.5 1-1 1A9 9 0 0 1 0 1c0-.5.5-1 1-1z" fill="#f2631c"/></symbol>
    <symbol id="i-mail" viewBox="0 0 10 10"><rect x="0" y="2" width="10" height="6" fill="#f2631c"/><path d="M0 2l5 3.5L10 2" fill="none" stroke="#fff" stroke-width="1"/></symbol>
    <symbol id="i-web" viewBox="0 0 10 10"><circle cx="5" cy="5" r="4.5" fill="#f2631c"/><path d="M.5 5h9M5 .5v9" stroke="#fff" stroke-width=".8"/></symbol>
    <symbol id="i-tag" viewBox="0 0 10 10"><rect x=".5" y="2.5" width="9" height="5" rx="2.5" fill="none" stroke="#8a8fc4" stroke-width="1"/></symbol>
  </defs>
</svg>

<section class="piece card-front">
  <div class="wordmark"><i></i>VELTA HOME</div>
  <div class="panel">
    <div class="name">MARCO RINALDI</div>
    <div class="role">President</div>
    <div class="address">Via del Mulino 24<br>I-39100 Valdora (Bz)<br>REA-VWV Nr. Bz 315720<br>P.I.-MwSt. 04187365520</div>
    <div class="contacts">
      <div class="contact"><svg class="icon"><use href="#i-phone"/></svg>+39 340 5521873</div>
      <div class="contact"><svg class="icon"><use href="#i-mail"/></svg>office@veltahome.srl</div>
      <div class="contact"><svg class="icon"><use href="#i-web"/></svg>www.veltahome.srl</div>
      <div class="contact"><svg class="icon"><use href="#i-tag"/></svg>info.veltahome@pec.it</div>
      <div class="contact"><svg class="icon"><use href="#i-tag"/></svg>K7RTQW2</div>
    </div>
  </div>
</section>

<section class="piece card-back">
  <div class="wordmark"><i></i>VELTA HOME</div>
</section>

<section class="piece letterhead">
  <div class="wordmark"><i></i>VELTA HOME</div>
  <div class="address">Via del Mulino 24<br>I-39100 Valdora (Bz)<br>REA-VWV Nr. Bz 315720<br>P.I.-MwSt. 04187365520</div>
  <div class="divider"></div>
  <div class="contacts">
    <div class="contact"><svg class="icon"><use href="#i-phone"/></svg>+39 340 5521873</div>
    <div class="contact"><svg class="icon"><use href="#i-mail"/></svg>office@veltahome.srl</div>
    <div class="contact"><svg class="icon"><use href="#i-tag"/></svg>info.veltahome@pec.it</div>
    <div class="contact"><svg class="icon"><use href="#i-tag"/></svg>K7RTQW2</div>
  </div>
  <div class="watermark"></div>
  <div class="body">
    <div class="greeting">Dear Mr. Ferri,</div>
    <p>Lorem ipsum dolor sit amet, consectetur adipiscing elit. Donec orci purus, luctus vitae dignissim eu, iaculis sed purus. Vivamus faucibus, ipsum nec aliquet viverra, leo mauris condimentum ligula, sit amet sagittis enim ligula quis arcu. Nam egestas tortor id nisi porttitor mattis. In tortor ante, ultricies in suscipit a, tempus non massa. Vivamus et auctor mi. Fusce vel massa nulla. Phasellus nec eros mauris, et scelerisque orci.</p>
    <p>Donec malesuada orci vitae nulla accumsan porta a id massa. Quisque accumsan iaculis magna sit amet fringilla. Maecenas consequat, magna eget tincidunt semper, odio nibh rutrum mi, id feugiat ante nisi eu risus. Vestibulum nunc orci, rhoncus a placerat in, ultricies in mi. Cras mattis varius eros, vel fringilla nisi suscipit eget. Quisque scelerisque sagittis nulla at porttitor.</p>
    <p>Sed id augue vitae urna euismod commodo aliquet a quam. Pellentesque arcu velit, cursus et malesuada ut, consequat et diam. Nullam erat sem, rhoncus id ullamcorper vitae, rhoncus et arcu. In ultricies ultricies nulla, ut rutrum nisi iaculis at. Donec eu magna a metus ornare faucibus. Fusce aliquet faucibus ultricies. Morbi semper, est id tincidunt gravida, sem arcu adipiscing lacus, ac bibendum nulla leo eu purus. Quisque nec diam sed risus consectetur accumsan quis quis nibh. Vestibulum id purus lorem.</p>
    <p>It is a long established fact that a reader will be distracted by the readable content of a page when looking at its layout. The point of using Lorem Ipsum is that it has a more-or-less normal distribution of letters, as opposed to using 'Content here, content here', making it look like readable English. Many desktop publishing packages</p>
  </div>
  <div class="closing">Sincerely,</div>
  <div class="signature" role="img" aria-label="Handwritten signature"></div>
  <div class="signer">Marco Rinaldi<small>CEO/ Founder</small></div>
  <div class="footer"><div>www.veltahome.srl</div></div>
</section>

<section class="piece envelope-back">
  <svg class="flap" viewBox="0 0 401 67" aria-hidden="true"><path d="M0 0H401L394 48Q391 67 371 67H30Q10 67 8 48Z" fill="#14127a"/></svg>
  <div class="wordmark">VELTA HOME</div>
</section>

<section class="piece envelope-front">
  <div class="watermark"></div>
  <div class="window"></div>
  <div class="wordmark"><i></i>VELTA HOME</div>
  <div class="address">Via del Mulino 24<br>I-39100 Valdora (Bz)<br>REA-VWV Nr. Bz 315720<br>P.I.-MwSt. 04187365520</div>
  <div class="contacts">
    <div class="contact"><svg class="icon"><use href="#i-phone"/></svg>+39 340 5521873</div>
    <div class="contact"><svg class="icon"><use href="#i-mail"/></svg>office@veltahome.srl</div>
    <div class="contact"><svg class="icon"><use href="#i-tag"/></svg>info.veltahome@pec.it</div>
    <div class="contact"><svg class="icon"><use href="#i-tag"/></svg>K7RTQW2</div>
  </div>
  <div class="footer"><div>www.veltahome.srl</div></div>
</section>
</body>
</html>
```